Website Header for new website

We need a header/banner design for our revised website. Here is the link to our existing website lorimentaskel.me and to our new website in process seasonbrightway.us
Area of expertise is older adults, baby boomers and caregivers
This is an individual, professional website for a Speaker, Keynoter, Author, Brocaster

Target Market(s)

Event planners, broadcasters, publishers

Font styles to use
Serif

```html
<!DOCTYPE html>
<html lang="en">
<head>
<meta charset="utf-8">
<title>Lori Mentaskel – Website Header</title>
<link rel="stylesheet" href="https://fonts.googleapis.com/css2?family=Alegreya:wght@400;700&family=Alegreya+Sans:wght@700&family=Libre+Baskerville&display=swap">
<style>
  :root {
    --white: #ffffff;
    --ink: #1a1a1a;
    --blue-deep: #0a4f9e;
    --blue-mid: #1565c0;
    --blue-bright: #1e80e0;
    --blue-stripe: #0d5cb6;
    --blue-edge: #063f85;
    --rule: rgba(255,255,255,0.75);
    --portrait-warm: #d9662a;
    --portrait-dark: #5a3a2a;
  }
  * { margin: 0; padding: 0; box-sizing: border-box; }
  html, body { width: 1200px; height: 458px; overflow: hidden; background: var(--white); }
  .header { position: relative; width: 1200px; height: 458px; background: var(--white); }

  .topbar { position: absolute; left: 0; top: 0; width: 1200px; height: 62px; background: var(--white); }
  .wordmark {
    position: absolute; left: 20px; top: 12px; height: 34px; padding: 0 15px;
    border: 1.5px solid var(--ink);
    font-family: "Libre Baskerville", serif; font-size: 15px; line-height: 31px;
    color: var(--ink); letter-spacing: 0.3px;
  }

  .hero { position: absolute; left: 0; top: 62px; width: 1200px; height: 396px; }
  .hero-shapes { position: absolute; inset: 0; }

  .portrait { position: absolute; left: 100px; top: 12px; width: 232px; height: 384px; }

  .name-box {
    position: absolute; left: 356px; top: 40px; width: 297px; height: 52px;
    border: 1.5px solid var(--white);
    font-family: "Alegreya", serif; font-weight: 700; font-size: 33px;
    color: var(--white); text-align: center; line-height: 48px;
  }
  .divider { position: absolute; left: 356px; top: 170px; width: 844px; height: 1px; background: var(--rule); }

  .roles { position: absolute; top: 184px; list-style: none;
    font-family: "Alegreya", serif; font-size: 21px; line-height: 31.5px; color: var(--white); }
  .roles.col-a { left: 356px; }
  .roles.col-b { left: 599px; }

  .featured-label {
    position: absolute; left: 806px; top: 76px; width: 76px; height: 16px;
    border: 1px solid var(--white);
    font-family: "Alegreya Sans", sans-serif; font-weight: 700; font-size: 8.5px;
    letter-spacing: 0.8px; color: var(--white); text-align: center; line-height: 14px;
  }
  .badges { position: absolute; left: 806px; top: 100px; display: flex; gap: 10.5px; }
  .badge { width: 53px; height: 54px; background: var(--white); border-radius: 6px; }
</style>
</head>
<body>
<div class="header">
  <div class="topbar">
    <div class="wordmark">LORI MENTASKEL</div>
  </div>

  <div class="hero">
    <svg class="hero-shapes" width="1200" height="396" viewBox="0 0 1200 396" role="img" aria-label="Blurred photo of a conference audience in blue tones">
      <defs>
        <linearGradient id="audience" x1="0" y1="0" x2="1" y2="1">
          <stop offset="0" stop-color="#0f5fb5"/>
          <stop offset="0.5" stop-color="#1a72cf"/>
          <stop offset="1" stop-color="#1668c2"/>
        </linearGradient>
      </defs>
      <polygon points="150,0 1200,0 1200,148 1092,396 0,396 0,352" fill="url(#audience)"/>
      <polygon points="150,0 332,0 160,396 0,396 0,352" fill="var(--blue-stripe)"/>
      <polygon points="1200,120 1200,148 1092,396 1055,396" fill="var(--blue-edge)"/>
      <polygon points="0,0 150,0 0,352" fill="var(--white)"/>
      <polygon points="1200,148 1200,396 1092,396" fill="var(--white)"/>
    </svg>

    <svg class="portrait" viewBox="0 0 232 384" role="img" aria-label="Portrait of the speaker in an orange blazer and patterned skirt">
      <defs>
        <linearGradient id="portraitTone" x1="0" y1="0" x2="0" y2="1">
          <stop offset="0" stop-color="#c9a06e"/>
          <stop offset="0.35" stop-color="var(--portrait-warm)"/>
          <stop offset="0.75" stop-color="#b9532a"/>
          <stop offset="1" stop-color="var(--portrait-dark)"/>
        </linearGradient>
      </defs>
      <path d="M116,0 C150,0 166,30 162,70 L168,112 C200,120 226,150 232,200 L232,384 L0,384 L0,210 C6,150 30,120 64,112 L70,70 C66,30 82,0 116,0 Z" fill="url(#portraitTone)" opacity="0.9"/>
    </svg>

    <div class="name-box">Lori Mentaskel</div>

    <div class="featured-label">FEATURED ON</div>
    <div class="badges">
      <div class="badge"></div><div class="badge"></div><div class="badge"></div>
      <div class="badge"></div><div class="badge"></div><div class="badge"></div>
    </div>

    <div class="divider"></div>

    <ul class="roles col-a">
      <li>Dynamic Keynoter</li>
      <li>Motivating Speaker</li>
      <li>Influential Broadcaster</li>
    </ul>
    <ul class="roles col-b">
      <li>Prolific Author</li>
      <li>Enterainting Blogger</li>
      <li>Effective Trainer</li>
    </ul>
  </div>
</div>
</body>
</html>
```